BUilding Fascia Signage

I got the logo, now, I want to design the Fascia Signage for my shop.
Fasica signage is 5565mm x 470mmH
Need idea how to put the logo, text, colour to the fascia signage.
need something catching.
can add more decorate line.
may try with Black background and white background

Design & Build

```html
<!DOCTYPE html>
<html lang="en">
<head>
<meta charset="utf-8">
<title>Ravel Building Group – Fascia Sign</title>
<link href="https://fonts.googleapis.com/css2?family=Bebas+Neue&display=swap" rel="stylesheet">
<style>
  :root {
    --page-bg: #c2c2c2;
    --sign-black: #050505;
    --sign-blue: #3a86f5;
    --sign-white: #ffffff;
  }
  html, body {
    margin: 0;
    padding: 0;
    width: 1200px;
    height: 778px;
    overflow: hidden;
    background: var(--page-bg);
  }
  .canvas {
    width: 1200px;
    height: 778px;
    display: flex;
    align-items: center;
    justify-content: center;
  }
  .fascia-sign {
    display: block;
    width: 1156px;
    height: 98px;
    box-shadow: 0 3px 6px rgba(0,0,0,0.35);
  }
  .sign-text {
    font-family: "Bebas Neue", "Oswald", sans-serif;
  }
  .fill-black { fill: var(--sign-black); }
  .fill-blue { fill: var(--sign-blue); }
  .fill-white { fill: var(--sign-white); }
</style>
</head>
<body>
  <main class="canvas">
    <svg class="fascia-sign" viewBox="0 0 1445 122" xmlns="http://www.w3.org/2000/svg" role="img" aria-label="Ravel Building Group fascia sign">
      <rect class="fill-black sign-base" x="0" y="0" width="1445" height="122"/>
      <polygon class="fill-blue top-stripe" points="258,0 1445,0 1445,13 254,13"/>
      <polygon class="fill-blue divider-stripe" points="210,122 250,10 266,10 226,122"/>
      <polygon class="fill-blue bottom-stripe" points="0,112 214,112 210,122 0,122"/>
      <polygon class="fill-white tagline-panel" points="300,35 1168,35 1138,122 244,122"/>
      <polygon class="fill-blue phone-panel" points="1168,35 1445,35 1445,122 1138,122"/>

      <g class="brand-block">
        <rect class="fill-blue brand-mark" x="40" y="30" width="14" height="14"/>
        <text class="sign-text fill-white brand-name" x="118" y="68" font-size="44" text-anchor="middle">RAVEL</text>
        <text class="sign-text fill-white brand-name" x="118" y="94" font-size="19" text-anchor="middle" letter-spacing="1">BUILDING GROUP</text>
      </g>

      <text class="sign-text fill-blue tagline" x="327" y="103" font-size="72" textLength="806" lengthAdjust="spacingAndGlyphs">YOUR HOME OUR HEART BUILT WITH PURE CARE</text>
      <text class="sign-text fill-white phone-number" x="1197" y="100" font-size="66" textLength="212" lengthAdjust="spacingAndGlyphs">0400 555 123</text>
    </svg>
  </main>
</body>
</html>
```